Stationery Design
Letterhead, Envelope, Business Card, Email signature design
I need single sided standard sized Business Card [3.5" x 2"]
Myriad Pro
Professional
Corisse Pallant
Brand Manager
4127 Dunford Avenue
Burnaby, B.C. V3K 8T2
604-281-7734 ext. 120
corisse@brightfernco.ca
brightfernco.ca
We are a family-owned school photography company in Western Canada. We've just had a new logo and website designed and need some new stationery.
This is the .ai file we would like to use for the stationery design. Please refer to our website, brightfernco.ca, for more information about our brand.

```html
<!DOCTYPE html>
<html lang="en">
<head>
<meta charset="utf-8">
<title>Bright Fern Co – Business Card</title>
<link rel="stylesheet" href="https://fonts.googleapis.com/css2?family=Source+Sans+3:ital,wght@0,400;0,600;0,700;1,400&display=swap">
<style>
  :root {
    --bg: #2b2b2b;
    --card: #ffffff;
    --ink: #3a3a3a;
    --ink-soft: #5a5a5a;
    --muted: #8a8a8a;
    --accent: #1ea3c6;
    --rule: #cfcfcf;
    --band-grey: #9a9a9a;
  }
  html, body {
    margin: 0;
    padding: 0;
    width: 1200px;
    height: 780px;
    overflow: hidden;
    background: var(--bg);
    font-family: "Source Sans 3", "Myriad Pro", Arial, sans-serif;
  }
  .business-card {
    position: absolute;
    left: 75px;
    top: 90px;
    width: 1050px;
    height: 600px;
    background: var(--card);
    border-radius: 30px;
    overflow: hidden;
    box-shadow: 0 10px 30px rgba(0,0,0,.35);
  }
  .brand {
    position: absolute;
    left: 250px;
    top: 110px;
    display: flex;
    align-items: center;
    gap: 22px;
  }
  .brand-mark {
    width: 64px;
    height: 64px;
    background: var(--accent);
  }
  .brand-name {
    font-size: 66px;
    font-weight: 700;
    color: var(--ink);
    letter-spacing: -1px;
    line-height: 1;
  }
  .divider {
    position: absolute;
    left: 510px;
    top: 260px;
    width: 2px;
    height: 230px;
    background: var(--rule);
  }
  .person {
    position: absolute;
    left: 215px;
    top: 270px;
    text-align: center;
    width: 260px;
  }
  .person-name {
    font-size: 32px;
    font-weight: 700;
    color: var(--accent);
    margin: 0;
    line-height: 1.1;
  }
  .person-title {
    font-size: 21px;
    font-style: italic;
    color: var(--muted);
    margin: 4px 0 0;
  }
  .address {
    position: absolute;
    left: 215px;
    top: 420px;
    font-size: 22px;
    color: var(--ink-soft);
    line-height: 1.3;
    margin: 0;
    font-style: normal;
  }
  .contacts {
    position: absolute;
    left: 545px;
    top: 245px;
    list-style: none;
    margin: 0;
    padding: 0;
  }
  .contacts li {
    display: flex;
    align-items: center;
    gap: 12px;
    height: 37px;
    font-size: 22px;
    color: var(--ink-soft);
  }
  .contacts svg {
    width: 22px;
    height: 22px;
    fill: var(--accent);
    flex: none;
  }
  .band-grey {
    position: absolute;
    left: 0;
    right: 0;
    bottom: 44px;
    height: 5px;
    background: var(--band-grey);
  }
  .band-accent {
    position: absolute;
    left: 0;
    right: 0;
    bottom: 0;
    height: 38px;
    background: var(--accent);
  }
</style>
</head>
<body>
  <div class="business-card">
    <div class="brand">
      <div class="brand-mark"></div>
      <div class="brand-name">BRIGHT FERN CO</div>
    </div>

    <div class="person">
      <p class="person-name">Corisse Pallant</p>
      <p class="person-title">Brand Manager</p>
    </div>

    <address class="address">4127 Dunford Avenue<br>Burnaby, B.C. V3K 8T2</address>

    <div class="divider"></div>

    <ul class="contacts">
      <li>
        <svg viewBox="0 0 24 24"><path d="M6.6 10.8a15 15 0 0 0 6.6 6.6l2.2-2.2a1 1 0 0 1 1-.25 11.4 11.4 0 0 0 3.6.57 1 1 0 0 1 1 1V20a1 1 0 0 1-1 1A17 17 0 0 1 3 4a1 1 0 0 1 1-1h3.5a1 1 0 0 1 1 1c0 1.25.2 2.45.57 3.57a1 1 0 0 1-.25 1z"/></svg>
        (T) 1-888-502-3176
      </li>
      <li>
        <svg viewBox="0 0 24 24"><path d="M6.6 10.8a15 15 0 0 0 6.6 6.6l2.2-2.2a1 1 0 0 1 1-.25 11.4 11.4 0 0 0 3.6.57 1 1 0 0 1 1 1V20a1 1 0 0 1-1 1A17 17 0 0 1 3 4a1 1 0 0 1 1-1h3.5a1 1 0 0 1 1 1c0 1.25.2 2.45.57 3.57a1 1 0 0 1-.25 1z"/></svg>
        604-281-7734 ext. 120
      </li>
      <li>
        <svg viewBox="0 0 24 24"><path d="M8 1h8a2 2 0 0 1 2 2v18a2 2 0 0 1-2 2H8a2 2 0 0 1-2-2V3a2 2 0 0 1 2-2zm0 3v14h8V4zm4 15.5a1 1 0 1 0 0 2 1 1 0 0 0 0-2z"/></svg>
        604-592-4418
      </li>
      <li>
        <svg viewBox="0 0 24 24"><path d="M6 2h9l3 3v4H6zM3 10h18a1 1 0 0 1 1 1v8a1 1 0 0 1-1 1H3a1 1 0 0 1-1-1v-8a1 1 0 0 1 1-1zm3 3v2h5v-2zm10 0v2h2v-2z"/></svg>
        604-281-7790
      </li>
      <li>
        <svg viewBox="0 0 24 24"><path d="M12 2a10 10 0 1 0 5 18.66l-1-1.73A8 8 0 1 1 20 12v1a2 2 0 0 1-4 0V7h-2v.8A5 5 0 1 0 16.3 15a4 4 0 0 0 5.7-2v-1A10 10 0 0 0 12 2zm0 13a3 3 0 1 1 0-6 3 3 0 0 1 0 6z"/></svg>
        corisse@brightfernco.ca
      </li>
      <li>
        <svg viewBox="0 0 24 24"><circle cx="12" cy="12" r="10"/></svg>
        brightfernco.ca
      </li>
    </ul>

    <div class="band-grey"></div>
    <div class="band-accent"></div>
  </div>
</body>
</html>
```